Awesome business card design needed

We need a new business card design to go with our new logo.
We are a web development agency that specialises in highly complex back-end integrations as opposed to design, our customers are retailers, hotels, hospitals and any other organisation that has a large online marketing department.
Take a look at our website - www.kotravelu.com for some inspiration.
We want our new business cards to exude class, professionalism and style.
We are likely to choose a high-end card to print them on but we want the design of the card itself to really turn heads.
We have no specific colour requirements, the logo as you will see is a turquoise colour R89 G171 B167 #59aba7 but it can also be in white if you want to make the colour of the card something different.
The information on the card should be:
Name
Position
Tel
email
Potentially a double sided card could have our web address, twitter and FB links.

```html
<!DOCTYPE html>
<html lang="en">
<head>
<meta charset="utf-8">
<title>Kotravelu business card</title>
<link rel="stylesheet" href="https://fonts.googleapis.com/css2?family=Arimo:wght@400;700&display=swap">
<style>
  :root {
    --teal: #59aba7;
    --teal-panel: rgba(89, 171, 167, 0.88);
    --night-deep: #05070f;
    --night-blue: #1a2a6b;
    --night-glow: #4a63c9;
    --card-white: #ffffff;
    --card-shade: #ececec;
    --ink: #111111;
    --backdrop: #d9d9d9;
  }
  * { box-sizing: border-box; margin: 0; padding: 0; }
  html, body {
    width: 1200px;
    height: 900px;
    overflow: hidden;
    background: var(--backdrop);
    font-family: "Arimo", Arial, sans-serif;
  }
  .stage {
    width: 1200px;
    height: 900px;
    display: flex;
    flex-direction: column;
    align-items: center;
    justify-content: center;
    gap: 44px;
  }
  .card {
    position: relative;
    width: 580px;
    height: 332px;
    overflow: hidden;
    box-shadow: 0 6px 18px rgba(0, 0, 0, 0.25);
  }

  /* Front side */
  .card-front { background: var(--night-deep); }
  .city-scene {
    position: absolute;
    inset: 0;
    background:
      linear-gradient(180deg, var(--night-deep) 0%, #0b1330 40%, var(--night-blue) 62%, var(--night-glow) 72%, #121d4d 86%, var(--night-deep) 100%);
  }
  .brand-panel {
    position: absolute;
    left: 128px;
    top: 36px;
    width: 320px;
    height: 168px;
    background: var(--teal-panel);
    color: #ffffff;
    display: flex;
    flex-direction: column;
    align-items: center;
    padding-top: 16px;
  }
  .brand-panel .wordmark {
    font-size: 50px;
    font-weight: 700;
    letter-spacing: 2px;
    line-height: 1;
  }
  .brand-panel .web-address {
    margin-top: 20px;
    font-size: 14px;
    letter-spacing: 2px;
  }
  .social-row {
    margin-top: 10px;
    display: flex;
    gap: 46px;
    font-size: 15px;
    letter-spacing: 1.5px;
  }
  .social-handle { display: flex; align-items: center; gap: 7px; }
  .social-handle .marker {
    width: 14px;
    height: 14px;
    background: #ffffff;
  }

  /* Back side */
  .card-back {
    background: linear-gradient(160deg, var(--card-white) 0%, var(--card-white) 55%, var(--card-shade) 100%);
  }
  .identity {
    position: absolute;
    left: 60px;
    top: 112px;
    display: flex;
    align-items: flex-end;
    gap: 18px;
  }
  .identity .wordmark {
    color: var(--teal);
    font-size: 58px;
    font-weight: 700;
    letter-spacing: 2px;
    line-height: 1;
  }
  .person { color: var(--ink); padding-bottom: 4px; }
  .person .name { font-size: 19px; letter-spacing: 0.5px; }
  .person .role { font-size: 12px; margin-top: 2px; }
  .contacts {
    position: absolute;
    left: 86px;
    bottom: 52px;
    display: flex;
    gap: 40px;
    font-size: 14px;
    color: var(--ink);
  }
  .contact { display: flex; align-items: center; gap: 5px; }
  .contact svg { width: 16px; height: 16px; }
</style>
</head>
<body>
<main class="stage">
  <section class="card card-front">
    <div class="city-scene" role="img" aria-label="Night city skyline reflected in water, overlaid with a blue mosaic grid"></div>
    <div class="brand-panel">
      <div class="wordmark">kotravelu</div>
      <div class="web-address">www.kotravelu.com</div>
      <div class="social-row">
        <span class="social-handle"><span class="marker"></span>kotravelu</span>
        <span class="social-handle"><span class="marker"></span>KoTravelu</span>
      </div>
    </div>
  </section>

  <section class="card card-back">
    <div class="identity">
      <div class="wordmark">kotravelu</div>
      <div class="person">
        <div class="name">MARA LINDQVIST</div>
        <div class="role">Director</div>
      </div>
    </div>
    <div class="contacts">
      <span class="contact">
        <svg viewBox="0 0 16 16" aria-hidden="true">
          <circle cx="8" cy="8" r="8" fill="var(--teal)"/>
          <path d="M5.2 4.2 L6.6 4 L7.3 5.8 L6.4 6.5 C6.9 7.6 7.7 8.5 8.9 9.1 L9.6 8.2 L11.4 8.9 L11.2 10.4 C8 10.6 5 7.6 5.2 4.2 Z" fill="#ffffff"/>
        </svg>
        0987 654 321
      </span>
      <span class="contact">
        <svg viewBox="0 0 16 16" aria-hidden="true">
          <circle cx="8" cy="8" r="7" fill="none" stroke="var(--teal)" stroke-width="1.6"/>
          <ellipse cx="8" cy="8" rx="3" ry="7" fill="none" stroke="var(--teal)" stroke-width="1.1"/>
          <line x1="1" y1="8" x2="15" y2="8" stroke="var(--teal)" stroke-width="1.1"/>
        </svg>
        mara@kotravelu.com
      </span>
    </div>
  </section>
</main>
</body>
</html>
```